Vantler Helps - Pellbrook Gives Advertising Flyer

We are a vantler club that has received funding to run a community food drive project. We need a flyer for our community project that stands out . Our community project is trying to obtain non- perishable food for low income families and the vulnerable from residents in the area.
This flyer will be need to be visible and posted on store front windows and anywhere else where local residents can see it and be informed about the project. We will need a high quality version to print and a PDF version that will be e-mailed for promotional activities.

Target Market(s)

Community

Font styles to use
Sans Serif

Requirements
Must have
• My project must have logos as specified.
Nice to have
• - Images
- eye catching and modern

```html
<!DOCTYPE html>
<html lang="en">
<head>
<meta charset="utf-8">
<title>Vantler Helps – Pellbrook Gives Food Drive Flyer</title>
<link rel="stylesheet" href="https://fonts.googleapis.com/css2?family=Montserrat:wght@400;600;700;800;900&display=swap">
<style>
  :root{
    --gold:#f2a516;
    --blue:#1c5da8;
    --navy:#1f2f6b;
    --red:#e0261c;
    --purple:#6b2c8e;
    --cream:#fde9a6;
    --cream-deep:#f9d36a;
    --panel:#2a3a86;
    --white:#ffffff;
    --ink:#2b2b2b;
    --bank:#8a1538;
  }
  *{box-sizing:border-box;margin:0;padding:0}
  html,body{width:859px;height:1200px;overflow:hidden;background:var(--white)}
  body{font-family:"Montserrat",Arial,sans-serif;color:var(--ink)}
  .flyer{position:relative;width:859px;height:1200px;overflow:hidden;background:var(--white)}

  .masthead{position:absolute;left:0;top:0;width:859px;height:186px}
  .masthead-mark{position:absolute;left:40px;top:34px;width:110px;height:110px;border-radius:50%;background:var(--gold)}
  .masthead-title{position:absolute;left:180px;top:22px;font-size:60px;font-weight:900;color:var(--gold);letter-spacing:1px;line-height:1}
  .masthead-sub{position:absolute;left:180px;top:82px;font-size:47px;font-weight:800;color:var(--blue);line-height:1}
  .masthead-url{position:absolute;left:300px;top:136px;font-size:22px;font-weight:700;color:var(--navy);letter-spacing:3px}

  .stage{position:absolute;left:0;top:186px;width:859px;height:920px;background:linear-gradient(180deg,var(--cream) 0%,var(--cream-deep) 100%)}
  .hero-photo{position:absolute;left:372px;top:186px;width:487px;height:560px;background:linear-gradient(160deg,#f6dfa0 0%,#d9c3a0 45%,#b84a3a 100%)}

  .headline{position:absolute;left:34px;top:226px;font-size:36px;font-weight:800;line-height:44px;color:var(--navy)}
  .headline .call{display:block;color:var(--red);font-weight:900}

  .partner-name{position:absolute;left:34px;top:494px;font-size:46px;font-weight:700;color:var(--purple)}
  .partner-about{position:absolute;left:34px;top:554px;width:320px;font-size:21px;line-height:30px;font-weight:600;color:var(--purple)}

  .thanks{position:absolute;left:34px;top:900px;width:282px;height:100px;background:var(--purple);color:var(--white);font-size:26px;font-weight:800;line-height:34px;padding:16px 20px}

  .appeal{position:absolute;left:458px;top:740px;width:390px;height:360px;background:var(--panel);border:4px solid var(--white);color:var(--white);text-align:center;padding:26px 22px}
  .appeal-title{font-size:32px;font-weight:900;line-height:40px}
  .appeal-text{margin-top:22px;font-size:22px;font-weight:600;line-height:30px}

  .supporters-label{position:absolute;left:34px;top:1074px;font-size:22px;font-weight:700;color:var(--navy)}
  .supporters{position:absolute;left:0;top:1110px;width:859px;height:90px;background:var(--white);display:flex;align-items:center;justify-content:space-around;padding:0 20px}
  .supporter{display:flex;align-items:center;gap:8px;font-size:17px;font-weight:700;color:var(--navy)}
  .supporter .dot{width:26px;height:26px;border-radius:50%;background:var(--gold)}
  .supporter.bank{background:var(--bank);color:var(--white);padding:10px 14px}
</style>
</head>
<body>
<main class="flyer">
  <header class="masthead">
    <div class="masthead-mark"></div>
    <div class="masthead-title">VANTLER HELPS</div>
    <div class="masthead-sub">PELLBROOK GIVES</div>
    <div class="masthead-url">www.vpg.org.au</div>
  </header>

  <section class="stage"></section>
  <div class="hero-photo" role="img" aria-label="Volunteer in a red cap and face mask holding a box full of pantry groceries"></div>

  <h1 class="headline">Food Security and<br>the COVID Crisis<br>in Pellbrook<span class="call">YOU CAN MAKE<br>A DIFFERENCE</span></h1>

  <div class="partner-name">kindhaven</div>
  <p class="partner-about">provides support to enhance the quality of life of people living in the Pellbrook and surrounding communities.</p>

  <div class="thanks">Thank you for your support!</div>

  <section class="appeal">
    <h2 class="appeal-title">CAN YOU HELP REFILL KINDHAVEN'S FOOD PANTRY?</h2>
    <p class="appeal-text">We need donations of non – perishable food items</p>
    <p class="appeal-text">Look out for our bags and information in your letter box</p>
  </section>

  <div class="supporters-label">Proudly supported by</div>
  <footer class="supporters">
    <div class="supporter"><span class="dot"></span>Vantler Pellbrook</div>
    <div class="supporter">Pellbrook</div>
    <div class="supporter bank">Corlow Bank</div>
    <div class="supporter"><span class="dot"></span>The Vantler Foundation</div>
  </footer>
</main>
</body>
</html>
```